Belford & Company

We are a boutique commercial real estate firm. For our Business card design - sleek, modern, yet high-end/classy. Please see our website: belfordandcompany.example for details.

We currently need 2 business card names and the ability to add/change the business card information -
Name, Title, Address, Office #, Mobile #, Fax, Email and company website.

Industry/Entity Type

Real Estate

Contact Information for Business Card

Business card design - sleek, modern, yet high-end/classy. Please see our website: belfordandcompany.example for details.

Also, we'd like to have our slogan "Precision Shapes Every Outcome." somewhere in there. We'd like to make some part of it raised or a different texture if possible.
Color #'s:
blue 19 36 128
light gray 222 222 221
dark gray 107 120 128

Also, we'd like to have our slogan "Precision Shapes Every Outcome." somewhere in there. We'd like to make some part of it raised or a different texture if possible - grey on one side and blue on the other - rounded edges preferred. Maybe either metal/silver/grey raised logo on the back. Thank you!!

Requirements
Must have
• Sleek, modern, clean and classy design

```html
<!DOCTYPE html>
<html lang="en">
<head>
<meta charset="utf-8">
<title>Belford &amp; Company — Business Card</title>
<link href="https://fonts.googleapis.com/css2?family=Lato:ital,wght@0,400;0,700;0,900;1,400&display=swap" rel="stylesheet">
<style>
  :root {
    --brand-blue: #2a3080;
    --brand-navy: #132480;
    --light-gray: #dededd;
    --dark-gray: #6b7880;
    --card-white: #f4f5f5;
    --text-gray: #555b60;
    --stage: #3a3a3c;
  }
  * { margin: 0; padding: 0; box-sizing: border-box; }
  html, body { width: 1200px; height: 891px; overflow: hidden; }
  body {
    background: var(--stage);
    font-family: "Lato", sans-serif;
    position: relative;
  }
  .card {
    position: absolute;
    top: 291px;
    width: 540px;
    height: 309px;
    border-radius: 22px;
    overflow: hidden;
    box-shadow: 0 10px 28px rgba(0,0,0,0.45);
  }
  /* Front */
  .card-front { left: 40px; background: var(--brand-blue); }
  .front-brand {
    position: absolute;
    left: 0; right: 0; top: 50%;
    transform: translateY(-50%);
    display: flex; align-items: center; justify-content: center; gap: 18px;
  }
  .brand-square { width: 34px; height: 34px; background: var(--light-gray); }
  .brand-name {
    font-family: "Lato", sans-serif;
    font-weight: 900;
    font-size: 38px;
    color: #ffffff;
    letter-spacing: 1px;
    text-transform: uppercase;
  }
  /* Back */
  .card-back { left: 620px; background: var(--card-white); }
  .holder { position: absolute; left: 34px; top: 26px; }
  .holder-name { font-size: 26px; color: var(--brand-navy); font-weight: 400; }
  .holder-name strong { font-weight: 700; }
  .holder-title { font-size: 12px; font-style: italic; color: var(--text-gray); margin-top: 1px; }
  .contact-list {
    position: absolute; left: 34px; top: 96px;
    list-style: none;
    font-size: 15px; color: var(--text-gray); line-height: 20px; letter-spacing: 0.6px;
  }
  .contact-list li { display: flex; align-items: flex-start; gap: 10px; }
  .contact-list svg { width: 12px; height: 12px; margin-top: 4px; flex: none; fill: var(--brand-navy); }
  .contact-list .address-line { padding-left: 22px; }
  .slogan-band {
    position: absolute; left: 0; right: 0; bottom: 0; height: 46px;
    background: var(--dark-gray);
    display: flex; align-items: center; justify-content: center;
    color: #ffffff; font-size: 16px; font-weight: 700; letter-spacing: 4.5px; text-transform: uppercase;
  }
</style>
</head>
<body>
  <section class="card card-front">
    <div class="front-brand">
      <span class="brand-square"></span>
      <span class="brand-name">Belford &amp; Company</span>
    </div>
  </section>

  <section class="card card-back">
    <div class="holder">
      <p class="holder-name">Alex <strong>Morgan</strong></p>
      <p class="holder-title">Title goes here</p>
    </div>
    <ul class="contact-list">
      <li><svg viewBox="0 0 12 12"><rect x="3" y="0" width="6" height="12" rx="1"/></svg>555-010-2468</li>
      <li><svg viewBox="0 0 12 12"><path d="M1 4 Q6 0 11 4 L9 6 L8 5 H4 L3 6 Z M2 7 H10 V12 H2 Z"/></svg>555-010-1357</li>
      <li><svg viewBox="0 0 12 12"><rect x="1" y="5" width="10" height="7"/><rect x="3" y="0" width="6" height="4"/></svg>555-010-1358</li>
      <li><svg viewBox="0 0 12 12"><path d="M0 2 H12 V10 H0 Z M0 2 L6 7 L12 2"/></svg>belfordandcompany.example</li>
      <li><svg viewBox="0 0 12 12"><circle cx="3.5" cy="8.5" r="3"/><circle cx="8.5" cy="3.5" r="3"/></svg>yourname@belfordandcompany.example</li>
      <li><svg viewBox="0 0 12 12"><path d="M6 0 L12 6 H10 V12 H2 V6 H0 Z"/></svg>Street address goes here,</li>
      <li class="address-line">Suite #210, Elm Plaza, NY 10021</li>
    </ul>
    <div class="slogan-band">Precision Shapes Every Outcome</div>
  </section>
</body>
</html>
```